Tri-fold Brochure Design for Banking Business

The brochure we have needs to be improved - more business like and more attractive. Logo file and brochure is attached. I would like to be able to edit the text after you get done. Your ideas and changes to text are welcome. See our website www.korvanbridgegrp.com for our theme. We can use indesign to edit the text after you complete. However, please make changes to the text we have in the design that it uploaded. Your comments and changes are welcome.

Target Market(s)

Human Resources and learning & development staff at the global investment banks - Pellham Trask, QWNR, etc.

Industry/Entity Type

Investment Banking

Logo Text

Korvan Bridge Group

Font styles to use
Serif
Sans Serif

Colors
33a6d7
0493ce
3277b5
fbf289
fdf9cf
fbee3e
0555a3
85acd3

Requirements
Must have
• Must be similar to our website www.korvanbridgegrp.com. Needs to be business-like, clean fonts, sharp design. Our logo - of course.
Nice to have
• City images - seems to be our theme.

```html
<!DOCTYPE html>
<html lang="en">
<head>
<meta charset="utf-8">
<title>Korvan Bridge Group – Tri-fold Brochure</title>
<link href="https://fonts.googleapis.com/css2?family=Oswald:wght@500;600&family=Arimo:ital,wght@0,400;0,700;1,700&display=swap" rel="stylesheet">
<style>
  :root{
    --navy:#1a4d97;
    --royal:#2a64b0;
    --ink-blue:#1d55a3;
    --sun:#fbe20a;
    --pale:#f1f6fb;
    --mist-top:#dbe6ee;
    --mist-bottom:#bccfdc;
    --white:#ffffff;
    --stage:#d9d9d9;
    --black:#111111;
  }
  *{box-sizing:border-box;margin:0;padding:0}
  html,body{width:1200px;height:899px;overflow:hidden;background:var(--stage)}
  body{font-family:"Arimo",Arial,sans-serif;position:relative}
  .brochure{position:absolute;left:30px;top:30px;width:1140px;height:839px;display:flex;box-shadow:0 6px 22px rgba(0,0,0,.25);background:var(--white)}
  .panel{position:relative;width:380px;height:100%;overflow:hidden}

  .ribbon{position:absolute;height:44px;background:var(--navy);color:var(--sun);font-family:"Oswald",sans-serif;font-weight:600;font-size:25px;letter-spacing:.5px;line-height:44px;padding-left:28px;text-transform:uppercase;clip-path:polygon(0 0,100% 0,88% 50%,100% 100%,0 100%)}
  .ribbon span{display:inline-block;transform:skewX(-10deg)}
  .ribbon.on-blue{background:var(--sun);color:var(--navy)}

  .copy{color:var(--ink-blue);font-size:15px;line-height:1.22}
  .copy p+p{margin-top:6px}

  /* left panel */
  .panel-why{background:var(--pale)}
  .panel-why .ribbon{left:0;top:34px;width:250px}
  .panel-why .copy{position:absolute;left:36px;top:100px;width:300px}
  .benefits{position:absolute;left:36px;top:228px;width:320px;list-style:none;color:var(--ink-blue);font-weight:700;font-style:italic;font-size:15px;line-height:1.2}
  .benefits li{position:relative;padding-left:30px;margin-bottom:10px}
  .benefits li::before{content:"";position:absolute;left:2px;top:3px;width:12px;height:12px;background:var(--sun);border:2px solid var(--navy)}
  .photo-meeting{position:absolute;left:0;bottom:0;width:380px;height:380px;background:linear-gradient(135deg,#e9eef4 0%,#9fb0c2 40%,#3e4b5c 75%,#20262f 100%)}

  /* middle panel */
  .panel-services{background:var(--navy)}
  .photo-training{position:absolute;left:0;top:0;width:380px;height:215px;background:linear-gradient(160deg,#7fb4e0 0%,#3f7fc0 50%,#163f7a 100%)}
  .panel-services .ribbon{left:0;top:215px;width:250px}
  .panel-services .copy{position:absolute;left:36px;top:285px;width:310px;color:var(--white);font-size:15.5px}
  .panel-services .copy p+p{margin-top:4px}

  /* right panel */
  .panel-team{background:linear-gradient(180deg,var(--mist-top),var(--mist-bottom) 70%)}
  .panel-team .ribbon{right:40px;top:40px;width:210px;padding-left:40px;clip-path:polygon(12% 0,100% 0,100% 100%,12% 100%,0 50%)}
  .panel-team .intro{position:absolute;left:40px;top:100px;width:300px;text-align:center;font-weight:700}
  .photo-team{position:absolute;left:0;top:200px;width:380px;height:270px;background:linear-gradient(180deg,#d3dfe8 0%,#a9bfd0 55%,#8eaac2 100%)}
  .panel-team .closing{position:absolute;left:40px;top:480px;width:300px;text-align:center;font-weight:700}

  /* shared footer band across middle + right */
  .footer-band{position:absolute;left:380px;top:548px;width:760px;height:291px}
  .footer-band svg{display:block}
  .logo{position:absolute;left:420px;top:738px;display:flex;align-items:center;gap:10px}
  .logo .mark{width:22px;height:22px;background:var(--navy)}
  .logo .name{font-family:"Arimo",Arial,sans-serif;font-weight:700;font-size:22px;color:var(--black);letter-spacing:.3px}
  .contact{position:absolute;left:800px;top:572px;width:340px;text-align:center;color:var(--white)}
  .contact .ask{font-size:17px}
  .contact h2{font-family:"Oswald",sans-serif;font-weight:600;font-size:30px;color:var(--sun);text-transform:uppercase;margin:2px 0}
  .contact h2 span{display:inline-block;transform:skewX(-10deg)}
  .contact .web{font-weight:700;font-size:18px}
  .address{position:absolute;left:800px;top:716px;width:340px;text-align:center;color:var(--navy);font-size:16px;line-height:1.3}
  .address .tel{font-size:19px;margin-top:4px}
</style>
</head>
<body>
<main class="brochure">
  <section class="panel panel-why">
    <div class="ribbon"><span>Why choose us?</span></div>
    <div class="copy">
      <p>Korvan Bridge Group is dedicated to providing you and your firm with the highest level of service.</p>
      <p>We provide dedicated sales and logistics support for each program to insure consistent, reliable results.</p>
    </div>
    <ul class="benefits">
      <li>Highly qualified, international pool of trainers</li>
      <li>Strong client relationship management and support</li>
      <li>Competitive pricing and flexibility</li>
      <li>Outcome driven approach directly matches your company's needs</li>
    </ul>
    <div class="photo-meeting" role="img" aria-label="Photo of business people shaking hands across a meeting table"></div>
  </section>

  <section class="panel panel-services">
    <div class="photo-training" role="img" aria-label="Photo of a businessman touching a digital training interface with icons for coaching, mentoring, skill and leadership"></div>
    <div class="ribbon on-blue"><span>Our services</span></div>
    <div class="copy">
      <p>Korvan Bridge Group provides best in class services for all our clients.</p>
      <p>We provide highly customized programs tailored to your specific requirements.</p>
      <p>Direct interaction between our clients, consulting trainers and client service staff ensures measurable outcomes for program participants.</p>
      <p>We facilitate learning outcomes using a blended methodology combining interactive analysis, hands-on experiential models, market simulations and a state-of-the-art learning management system.</p>
      <p>Our material databanks are continuously updated to insure accuracy and effectiveness of our services</p>
    </div>
  </section>

  <section class="panel panel-team">
    <div class="ribbon"><span>Our team</span></div>
    <p class="copy intro">Our Consulting Trainers are located globally and recognized by the industry as highly effective trainers and program facilitators</p>
    <div class="photo-team" role="img" aria-label="Photo of a team of business people standing on a globe ringed by city skylines"></div>
    <p class="copy closing">Korvan provides global expertise for our programs with local talent for program facilitation.</p>
  </section>

  <div class="footer-band">
    <svg width="760" height="291" viewBox="0 0 760 291" aria-hidden="true">
      <rect x="380" y="0" width="380" height="4" fill="#ffffff"/>
      <rect x="380" y="4" width="380" height="150" fill="#2a64b0"/>
      <rect x="0" y="120" width="380" height="171" fill="#ffffff"/>
      <polygon points="330,154 760,154 760,291 330,291 380,222" fill="#fbe20a"/>
      <polygon points="300,154 330,154 380,222 330,291 300,291" fill="#ffffff"/>
    </svg>
  </div>

  <div class="logo">
    <span class="mark"></span>
    <span class="name">Korvan Bridge Group</span>
  </div>

  <div class="contact">
    <p class="ask">Need more information?</p>
    <h2><span>Contact us!</span></h2>
    <p class="web">www.korvanbridgegrp.com</p>
  </div>

  <div class="address">
    <p>Unit 4B Harlow Point Tower</p>
    <p>218-224 Marlowe Rd, East Quay</p>
    <p class="tel">Tel: +852 3107 5826</p>
    <p>info@korvanbridgegrp.com</p>
  </div>
</main>
</body>
</html>
```